Modern Small Law Firm Website To Look Cutting Edge

I need a website design for a new, single-attorney law firm. The firm will be called "The Hollowmere Law Group." Our goal is to handle car accident and general personal injury lawsuits for individuals.

Our selling points are: (1) We charge less so you keep more; (2) We have experience and success trying and settling multi-million dollar cases; (3) We use modern technology to make the whole process simple, easy and hassle-free for clients.

Also because we are a one-man law firm, the clients will personally know the lawyer and have access to them. For that reason, I thought a good big tagline for the website would be "KNOW YOUR LAWYER"

I like the idea of splitting the website vertically down the middle, with the left side having a blue background, a picture of me, and big white lettering for the tagline, and the right side having a white background with blue lettering and headlines. I don't want navy blue or royal blue, but a more bright and eye-catching blue color. We can experiment with different shades.

I would be curious about how it could look with some minor orange accent coloring somewhere.

I need to feature prominently, probably in the top left corner, this phone number: 504-617-2093.

This will be used as much by mobile users as it would be by desktop/computer users.

The final design should communicate trust, convenience and cutting edge technology that leads to success.

Finally, I would be curious how we can have a sleek looking info submission box somewhere on the right side nearer the bottom that features different combinations of presenting these phrases: "QUICK QUESTION? QUICK ANSWER" The info submission button could say "Ask"

I am uploading two different pictures of me that can be used. The gray backgrounds are not necessary or good, if there is a way to cut them out that would be great. I can try and get that if needed.

Target Market(s)

Individuals who have been hurt by others, mostly in car accidents. They will be frustrated, inconvenienced and need to be soothed.

Industry/Entity Type

Legal

Number of Pages Required

1 page

Font styles to use
Sans Serif

Colors
0692cd
33a6d7
85cae6
faa54b
f78f20
3276b5

Requirements
Must have
• If you have started designing already, please note that the project description information is more important than the image that I uploaded originally. It has since been deleted.
• Also please now use the color photo that has been uploaded.
Nice to have
• I really want a clean and simple website design with not a lot of clutter. I'd like to avoid the typical law firm websites that you see that have tool bars across the top and basic borders/columns everywhere. It needs to grab your attention and look a little more cutting edge and different.
• Let's experiment with different eye-catching ways to present the three value propositions I noted.
• Also if the screen is split vertically with the left and right side being blue and white, maybe we can experiment with different ways that the two colors could fade into each other as opposed to just a line where one color starts and the other ends.
• And maybe the blue/white backgrounds could be textured somehow so that they don't appear flat. Perhaps we could try using differing shades of blue to give the appearance of pattern or 3D texture.
Should not have
• The basic picture/design I uploaded is just a suggestion, but there isn't really anything there.

```html
<!DOCTYPE html>
<html lang="en">
<head>
<meta charset="utf-8">
<title>The Hollowmere Law Group</title>
<link rel="stylesheet" href="https://fonts.googleapis.com/css2?family=Montserrat:wght@400;500;600;700&family=Lato:ital,wght@0,300;0,400;0,700;1,300&family=Oswald:wght@400;500&display=swap">
<style>
:root{
  --red:#ee2027;
  --ink:#1f1f1f;
  --text:#6a6a6a;
  --muted:#8c8c8c;
  --grey-band:#f1f1f1;
  --blue:#0052a5;
  --blue-light:#3a7fd0;
  --blue-form:#1a73e0;
  --orange:#f78f20;
  --orange-light:#faa54b;
  --footer:#454545;
  --footer-bottom:#393939;
  --footer-text:#d0d0d0;
  --white:#ffffff;
  --line:#dcdcdc;
}
*{box-sizing:border-box;margin:0;padding:0}
html,body{width:1200px;height:2225px;overflow:hidden;background:var(--white)}
body{position:relative;font-family:'Lato',sans-serif;color:var(--text)}
.abs{position:absolute}
svg{display:block}

/* header */
.brand{left:156px;top:22px;font-family:'Montserrat',sans-serif;font-weight:600;font-size:22px;color:var(--ink);letter-spacing:.2px}
.social{top:27px;left:664px;display:flex;gap:8px}
.social span{width:23px;height:23px;border-radius:50%;background:#c9c9c9;display:block}
.social span.active{background:var(--red)}
.header-call{left:828px;top:20px;display:flex;align-items:center;gap:8px;font-family:'Oswald',sans-serif;font-size:27px;color:#444}
.header-call .label{color:var(--red)}

/* nav */
.nav{left:0;top:80px;width:1200px;height:42px;background:var(--red)}
.nav ul{list-style:none;display:flex;position:absolute;left:156px;top:0;height:42px}
.nav li{font-family:'Montserrat',sans-serif;font-weight:600;font-size:11px;color:var(--white);letter-spacing:.3px;padding:0 21px;line-height:42px}
.nav li.current{background:#3a3a3a;color:var(--red);padding:0 15px}

/* hero */
.hero{left:0;top:122px;width:1200px;height:359px;background:linear-gradient(100deg,#7d8a72 0%,#a7aa98 30%,#8f8b84 55%,#4a5562 80%,#2e3746 100%)}
.hero-shade{left:0;top:122px;width:1200px;height:359px;background:linear-gradient(90deg,rgba(0,0,0,.28),rgba(0,0,0,.05) 60%)}
.hero-title{left:156px;top:240px;font-family:'Montserrat',sans-serif;font-weight:500;font-size:30px;color:var(--white)}
.hero-text{left:156px;top:291px;width:556px;font-size:14px;line-height:18px;color:var(--white)}
.hero-more{left:156px;top:341px;display:flex;align-items:center;gap:5px;font-family:'Montserrat',sans-serif;font-size:11px;letter-spacing:1px;color:var(--white)}
.arrow-left{left:84px;top:290px}
.arrow-right{left:1092px;top:290px}

/* testimonials */
.testimonials{left:0;top:481px;width:1200px;height:268px;background:var(--grey-band)}
.testi-title{left:156px;top:517px;font-family:'Montserrat',sans-serif;font-weight:600;font-size:14px;color:var(--ink)}
.testi-quote{left:156px;top:553px;width:510px;font-style:italic;font-weight:300;font-size:13.5px;line-height:18px;color:#555}
.avatar{left:156px;top:642px;width:76px;height:76px;border-radius:50%;border:4px solid var(--white);background:radial-gradient(circle at 50% 40%,#c9a08a,#6b4a3a);box-shadow:0 1px 4px rgba(0,0,0,.15)}
.testi-name{left:254px;top:670px;font-size:15px;color:var(--blue-form)}
.dots{left:618px;top:675px;display:flex;gap:3px}
.dots i{width:7px;height:7px;border-radius:50%;border:1px solid #888;display:block}
.dots i.on{background:#666}

/* quick form */
.quick{left:764px;top:400px;width:280px;height:413px}
.quick-head{left:764px;top:400px;width:280px;height:82px;background:linear-gradient(180deg,#2a86f0,#0f66d6);color:var(--white);text-align:center;padding-top:15px}
.quick-head .q1{font-family:'Oswald',sans-serif;font-size:19px;line-height:24px}
.quick-head .q2{font-family:'Lato',sans-serif;font-size:19px;line-height:26px}
.field{left:788px;width:232px;height:28px;border:1px solid var(--line);border-radius:3px;background:var(--white);font-size:11px;color:#888;padding:6px 8px}
.ask{left:868px;top:734px;width:72px;height:28px;background:var(--red);border-radius:3px;color:var(--white);font-family:'Montserrat',sans-serif;font-weight:600;font-size:12px;text-align:center;line-height:28px;letter-spacing:1px}

/* why */
.why-title{left:0;top:853px;width:1200px;text-align:center;font-family:'Montserrat',sans-serif;font-weight:600;font-size:23px;color:var(--ink)}
.value{width:260px;text-align:center}
.value svg{margin:0 auto}
.value h3{margin-top:18px;font-family:'Montserrat',sans-serif;font-weight:500;font-size:14px;letter-spacing:.8px;color:var(--ink)}
.value p{margin:9px auto 0;width:236px;font-size:12px;line-height:16px;color:var(--muted)}

/* about band */
.about{left:0;top:1191px;width:1200px;height:356px;background:var(--blue)}
.frame-back{left:156px;top:1258px;width:204px;height:205px;background:var(--blue-light);opacity:.75}
.frame-front{left:180px;top:1282px;width:204px;height:203px;background:var(--blue-light);opacity:.75}
.portrait-photo{left:180px;top:1282px;width:180px;height:180px;background:linear-gradient(180deg,#f4f4f4 0%,#eaeaea 45%,#2a3140 46%,#1c2230 100%)}
.about-title{left:415px;top:1262px;font-family:'Montserrat',sans-serif;font-weight:600;font-size:19px;color:var(--white);letter-spacing:.3px}
.about-sub{left:415px;top:1285px;font-family:'Montserrat',sans-serif;font-size:14px;color:var(--white)}
.about-text{left:415px;top:1318px;width:300px;font-size:12px;line-height:16px;color:var(--white)}
.about-more{left:415px;top:1455px;display:flex;align-items:center;gap:5px;font-family:'Montserrat',sans-serif;font-size:11px;letter-spacing:1px;color:var(--white)}

/* practice card */
.practice{left:765px;top:1162px;width:279px;height:418px;background:#f4f4f4;box-shadow:0 2px 10px rgba(0,0,0,.22)}
.practice-head{left:765px;top:1162px;width:279px;height:63px;background:linear-gradient(180deg,#3b3b3b,#2a2a2a);border-top:3px solid #1d1d1d;color:var(--white);font-family:'Montserrat',sans-serif;font-weight:600;font-size:23px;padding:14px 0 0 26px}
.practice-notch{left:804px;top:1223px}
.area{left:796px;width:220px}
.area h4{font-family:'Montserrat',sans-serif;font-weight:600;font-size:13.5px;color:var(--ink)}
.area p{margin-top:6px;width:192px;font-size:12px;line-height:15.4px;color:var(--muted)}
.practice-more{left:796px;top:1531px;display:flex;align-items:center;gap:5px;font-family:'Montserrat',sans-serif;font-size:11px;letter-spacing:1px;color:#444}

/* help */
.help-title{left:0;top:1653px;width:1200px;text-align:center;font-family:'Montserrat',sans-serif;font-weight:600;font-size:23px;color:var(--ink)}
.help-sub{left:0;top:1684px;width:1200px;text-align:center;font-size:19px;font-weight:300;color:var(--muted)}
.help-call{left:496px;top:1735px;width:183px;height:39px;border-radius:3px;background:linear-gradient(180deg,var(--orange-light),var(--orange));box-shadow:0 3px 6px rgba(0,0,0,.2);display:flex;align-items:center;gap:14px;padding-left:12px;font-family:'Montserrat',sans-serif;font-weight:600;font-size:16px;color:var(--white)}

/* footer */
.footer{left:0;top:1859px;width:1200px;height:302px;background:var(--footer)}
.footer-bottom{left:0;top:2161px;width:1200px;height:64px;background:var(--footer-bottom)}
.foot-heading{top:1920px;font-family:'Montserrat',sans-serif;font-weight:500;font-size:14px;letter-spacing:.8px;color:var(--white)}
.site-links{left:172px;top:1957px;font-size:12.5px;line-height:22.3px;color:var(--footer-text)}
.site-links li.current{color:var(--red)}
.news-field{left:460px;width:204px;height:27px;border:1px solid #8a8a8a;border-radius:3px;font-size:11px;color:#bbb;padding:6px 9px}
.news-submit{left:460px;top:2048px;width:88px;height:28px;background:#222;border-radius:3px;color:var(--white);font-family:'Montserrat',sans-serif;font-weight:600;font-size:11px;letter-spacing:1px;text-align:center;line-height:28px}
.contact{left:764px;top:1957px;font-size:12.5px;line-height:16px;color:var(--footer-text)}
.get-social{left:764px;top:2071px;font-size:12.5px;color:var(--footer-text)}
.foot-social{left:764px;top:2098px;display:flex;gap:7px}
.foot-social span{width:25px;height:25px;border-radius:50%;background:#9a9a9a;display:block}
.copyright{left:156px;top:2186px;font-size:11.5px;color:#9c9c9c}
.to-top{left:1006px;top:2181px}
</style>
</head>
<body>

<!-- header -->
<div class="abs brand">The Hollowmere Law Group</div>
<div class="abs social"><span></span><span class="active"></span><span></span><span></span></div>
<div class="abs header-call">
  <span class="label">Call</span>
  <svg width="30" height="30" viewBox="0 0 30 30"><circle cx="15" cy="15" r="13" fill="none" stroke="#ee2027" stroke-width="2.4"/><path d="M10 9c1-1 2-1 2.6 0l1.4 2.4c.4.7.2 1.4-.4 1.8l-.9.6c.8 1.8 2 3 3.7 3.8l.6-.9c.4-.6 1.2-.8 1.8-.4l2.4 1.4c.9.6.9 1.6 0 2.6-1.3 1.4-3.300 1.6-5.300.5-2.6-1.4-4.6-3.5-5.9-6.1-1-2-.8-4.3 0-5.7z" fill="#ee2027"/></svg>
  <span>504-617-2093</span>
</div>

<!-- navigation -->
<nav class="abs nav">
  <ul>
    <li class="current">HOME</li>
    <li>ABOUT MY FIRM</li>
    <li>ATTORNEY BIO</li>
    <li>PERSONAL INJURY</li>
    <li>TESTIMONIALS</li>
    <li>BLOG</li>
    <li>CONTACT US</li>
  </ul>
</nav>

<!-- hero -->
<div class="abs hero" role="img" aria-label="Photo of a distressed woman sitting beside a damaged car after an accident"></div>
<div class="abs hero-shade"></div>
<h1 class="abs hero-title">Goals and Belief</h1>
<p class="abs hero-text">We Belive in “KNOW YOUR LAWYER” and with this serving clients who needs to handle car accident and general personal injury lawsuits.</p>
<div class="abs hero-more"><svg width="10" height="10" viewBox="0 0 10 10"><circle cx="5" cy="5" r="5" fill="#fff"/><path d="M4 2.8 6.2 5 4 7.2" stroke="#777" stroke-width="1.4" fill="none"/></svg>READ MORE</div>
<svg class="abs arrow-left" width="24" height="20" viewBox="0 0 24 20"><path d="M22 10H4M11 2 3 10l8 8" stroke="#fff" stroke-width="3" fill="none"/></svg>
<svg class="abs arrow-right" width="24" height="20" viewBox="0 0 24 20"><path d="M2 10h18M13 2l8 8-8 8" stroke="#ee2027" stroke-width="3" fill="none"/></svg>

<!-- testimonials -->
<section class="abs testimonials"></section>
<h2 class="abs testi-title">Client Testimonials</h2>
<p class="abs testi-quote">“ Hiring Daniel Arvane was one of the best decisions of my life. From the first moment I spoke to Daniel, I knew he was the attorney for me. I felt he was honest and caring. He also took extra care...”</p>
<div class="abs avatar" role="img" aria-label="Client portrait"></div>
<div class="abs testi-name">— Carla. M.</div>
<div class="abs dots"><i></i><i></i><i class="on"></i><i></i><i></i></div>

<!-- quick question form -->
<svg class="abs quick" width="280" height="413" viewBox="0 0 280 413" style="filter:drop-shadow(0 2px 6px rgba(0,0,0,.18))"><path d="M0 0H280V348L140 413 0 348Z" fill="#fff"/></svg>
<div class="abs quick-head">
  <div class="q1">“Quick Question? Quick Answer”</div>
  <div class="q2">Contact Us Today!</div>
</div>
<div class="abs field" style="top:505px">Name</div>
<div class="abs field" style="top:542px">Email</div>
<div class="abs field" style="top:580px">Phone</div>
<div class="abs field" style="top:617px;height:84px">Your Question ...</div>
<div class="abs ask">ASK</div>

<!-- value propositions -->
<h2 class="abs why-title">Why - The Hollowmere Law Group?</h2>
<div class="abs value" style="left:167px;top:944px">
  <svg width="50" height="62" viewBox="0 0 50 62"><g fill="none" stroke="#ee2027" stroke-width="2.6" stroke-linejoin="round"><rect x="15" y="3" width="20" height="13" rx="2"/><circle cx="25" cy="9.5" r="3"/><path d="M8 60V36l10-12h14v10l-8 2v8"/><path d="M32 24l8 4v14l-8 10H20"/></g></svg>
  <h3>LESS CHARGE</h3>
  <p>We charge less to our clients so they keep more for future</p>
</div>
<div class="abs value" style="left:471px;top:944px">
  <svg width="50" height="62" viewBox="0 0 50 62"><g fill="none" stroke="#ee2027" stroke-width="2.6" stroke-linejoin="round"><path d="M25 3l5 4 6-1 2 6 6 3-2 6 3 5-5 4-1 6-6 1-3 5-5-3-5 3-3-5-6-1-1-6-5-4 3-5-2-6 6-3 2-6 6 1z"/><circle cx="25" cy="26" r="9"/><path d="M15 42 9 58l7-3 4 6 5-12M35 42l6 16-7-3-4 6-5-12"/></g></svg>
  <h3>EXPERIENCE &amp; SUCCESS</h3>
  <p>We have experience and success trying and settling multi-million dollar cases</p>
</div>
<div class="abs value" style="left:775px;top:944px">
  <svg width="56" height="62" viewBox="0 0 56 62"><g fill="none" stroke="#ee2027" stroke-width="2.6" stroke-linejoin="round"><path d="M24 6h8l1.5 6.5 5 2 5.5-3.5 5.5 5.5-3.5 5.5 2 5 6.5 1.5v8l-6.5 1.5-2 5 3.5 5.5-5.5 5.5-5.5-3.5-5 2L32 56h-8l-1.5-6.5-5-2-5.5 3.5-5.5-5.5 3.5-5.5-2-5L2 35v-8l6.5-1.5 2-5L7 15l5.5-5.5 5.5 3.5 5-2z"/><circle cx="28" cy="31" r="9"/></g></svg>
  <h3>USE MODERN TECHNOLOGY</h3>
  <p>We use modern technology to make the whole process simple, easy and hassle-free</p>
</div>

<!-- about band -->
<section class="abs about"></section>
<div class="abs frame-back"></div>
<div class="abs frame-front"></div>
<div class="abs portrait-photo" role="img" aria-label="Portrait of the attorney in a suit and tie"></div>
<h2 class="abs about-title">“KNOW YOUR LAWYER”</h2>
<div class="abs about-sub">About Us</div>
<p class="abs about-text">Lorem Ipsum is simply dummy text of the printing and typesetting industry. Lorem Ipsum has been the industry's standard dummy text ever since the 1500s, when an unknown printer took a galley of type and scrambled it to make a type specimen book. It has survived not only five centuries, but also the leap into electronic typesetting, ...</p>
<div class="abs about-more"><svg width="10" height="10" viewBox="0 0 10 10"><circle cx="5" cy="5" r="5" fill="#fff"/><path d="M4 2.8 6.2 5 4 7.2" stroke="#0052a5" stroke-width="1.4" fill="none"/></svg>READ MORE</div>

<!-- practice areas -->
<aside class="abs practice"></aside>
<div class="abs practice-head">Practice Areas</div>
<svg class="abs practice-notch" width="22" height="12" viewBox="0 0 22 12"><path d="M0 0h22L11 12z" fill="#2a2a2a"/></svg>
<div class="abs area" style="top:1263px">
  <h4>1. Car Accidents</h4>
  <p>Lorem Ipsum is simply dummy text of the printing and typesetting industry. Lorem Ipsum has been the industry's standard dummy text ever since the 1500s.</p>
</div>
<div class="abs area" style="top:1391px">
  <h4>2. General Personal Injury</h4>
  <p>Lorem Ipsum is simply dummy text of the printing and typesetting industry. Lorem Ipsum has been the industry's standard dummy text ever since the 1500s.</p>
</div>
<div class="abs practice-more"><svg width="10" height="10" viewBox="0 0 10 10"><circle cx="5" cy="5" r="5" fill="#333"/><path d="M4 2.8 6.2 5 4 7.2" stroke="#fff" stroke-width="1.4" fill="none"/></svg>READ MORE</div>

<!-- help -->
<h2 class="abs help-title">Can We Help You?</h2>
<p class="abs help-sub">We are available to answer your question 24/7 ...</p>
<div class="abs help-call">
  <svg width="20" height="20" viewBox="0 0 20 20"><circle cx="10" cy="10" r="9" fill="none" stroke="#fff" stroke-width="1.6"/><path d="M6.5 5.5c.7-.7 1.4-.7 1.8 0l1 1.6c.3.5.1 1-.3 1.2l-.6.4c.5 1.2 1.3 2 2.5 2.5l.4-.6c.3-.4.8-.5 1.2-.3l1.6 1c.6.4.6 1.1 0 1.8-.9.9-2.2 1-3.5.3a9 9 0 0 1-4-4c-.7-1.4-.5-2.9.1-3.9z" fill="#fff"/></svg>
  <span>504-617-2093</span>
</div>

<!-- footer -->
<footer class="abs footer"></footer>
<div class="abs footer-bottom"></div>
<h5 class="abs foot-heading" style="left:156px">SITE INFORMATION</h5>
<h5 class="abs foot-heading" style="left:460px">NEWSLETTER</h5>
<h5 class="abs foot-heading" style="left:764px">CONTACT INFO</h5>
<ul class="abs site-links">
  <li>Home</li><li class="current">About My Firm</li><li>Attorney Bio</li><li>Personal Injury</li><li>Testimonials</li><li>Blog</li><li>Contact</li>
</ul>
<div class="abs news-field" style="top:1962px">Name</div>
<div class="abs news-field" style="top:2000px">Email</div>
<div class="abs news-submit">SUBMIT</div>
<div class="abs contact">
  Hollowmere Law Group<br>4120 Larkspur Ave. NE Suite B<br>Fairhaven, NM 87190<br><br>
  Phone: 504-617-2093<br>Email: info@hollowmerelawgroup.com
</div>
<div class="abs get-social">Get Social:</div>
<div class="abs foot-social"><span></span><span></span><span></span><span></span></div>
<div class="abs copyright">© 2016 by Hollowmere Law Group. All rights reserved. &nbsp;Disclaimer &nbsp;/ &nbsp;Site Map &nbsp;/ &nbsp;Privacy Policy</div>
<svg class="abs to-top" width="25" height="25" viewBox="0 0 25 25"><circle cx="12.5" cy="12.5" r="11" fill="none" stroke="#aaa" stroke-width="1.6"/><path d="M12.5 18V8M8 12l4.5-4.5L17 12" stroke="#aaa" stroke-width="1.8" fill="none"/></svg>

</body>
</html>
```